Wedding Planning and Event Planners website

I am driven by perfection of my occupation and i look forward to having an attractive and contemporary website for an event and wedding planning group. We are located in the United States and Canada and we offer our services only in these two countries. My website is for people who are planning events such Church programs, weddings, musical concerts, Picnic, etc. My website should have imaginary of events such as weddings, musical concerts and picnic, etc.. I don't have any reference website because i want all designers to be creative and unique. I prefer blue,red,green,yellow colors.

Industry/Entity Type

Wedding

Coding

Coded - Design and coding required

```html
<!DOCTYPE html>
<html lang="en">
<head>
<meta charset="utf-8">
<title>Vowline Events — Event &amp; Wedding Planners</title>
<link href="https://fonts.googleapis.com/css2?family=Roboto:wght@400;500;700&family=Open+Sans:wght@400;600;700&display=swap" rel="stylesheet">
<style>
:root{
  --stage:#2a2a2c;
  --navy:#2b2640;
  --works:#2d2a40;
  --pink:#d8385e;
  --green:#a9c81e;
  --gold:#d9a85a;
  --blue:#4a8fb5;
  --white:#ffffff;
  --ink:#3a3a3a;
  --muted:#8a8a8a;
  --footer:#24213a;
}
*{box-sizing:border-box;margin:0;padding:0}
html,body{width:960px;height:1200px;overflow:hidden;background:var(--stage)}
body{font-family:"Open Sans",Arial,sans-serif;color:var(--ink)}
.page{position:absolute;left:287px;top:0;width:930px;height:2886px;transform:scale(.4158);transform-origin:0 0;background:var(--white);overflow:hidden}
.section{position:relative;width:930px}
.center{text-align:center}
.btn{display:inline-block;background:var(--pink);color:var(--white);font:700 8px/1 "Roboto",Arial,sans-serif;letter-spacing:1px;text-transform:uppercase;padding:7px 14px}
.boxed-title{display:inline-block;border:1.5px solid #9a9a9a;padding:6px 0;width:276px;font:500 14px/1 "Roboto",Arial,sans-serif;letter-spacing:3px;text-transform:uppercase;color:#333;text-align:center}
.body-copy{font-size:8px;line-height:14px;color:var(--muted);text-align:center;width:540px;margin:0 auto}

/* nav */
.nav{height:28px;background:var(--navy);display:flex;align-items:center;padding:0 180px 0 204px}
.brand{font:700 10px/1 "Roboto",Arial,sans-serif;color:var(--white)}
.nav-links{margin-left:auto;display:flex;gap:18px;font:700 7px/1 "Roboto",Arial,sans-serif;color:var(--white);text-transform:uppercase}

/* hero */
.hero{height:496px;background:linear-gradient(180deg,#3a2a1e 0%,#6b5236 35%,#4a3a2c 65%,#2c241e 100%)}
.hero-title{position:absolute;left:328px;top:324px;width:272px;height:40px;background:rgba(40,30,25,.55);border:1px solid rgba(255,255,255,.25);color:var(--white);font:700 28px/40px "Roboto",Arial,sans-serif;text-align:center}
.hero-actions{position:absolute;top:394px;left:0;width:100%;display:flex;justify-content:center;gap:14px}
.hero-actions .outline{background:transparent;border:2px solid var(--white);padding:5px 8px}

/* about */
.about{height:192px;padding-top:18px}
.about .body-copy{margin-top:24px}
.about .btn{margin-top:14px}

/* process */
.process{height:334px;background:radial-gradient(ellipse at 50% 40%,#5a4636 0%,#3a2c22 55%,#1e1814 100%);color:var(--white)}
.process h2{position:absolute;top:44px;width:100%;text-align:center;font:700 14px/1 "Roboto",Arial,sans-serif;letter-spacing:3px}
.process .rule{position:absolute;top:80px;left:458px;width:14px;height:1px;background:var(--gold)}
.steps{position:absolute;top:112px;left:194px;display:flex;gap:30px}
.step{width:118px;text-align:center}
.ring{width:60px;height:60px;border-radius:50%;border:2px solid var(--gold);margin:0 auto;display:flex;align-items:center;justify-content:center}
.ring.filled{background:var(--gold)}
.step h3{font:400 13px/1 "Roboto",Arial,sans-serif;margin-top:16px;text-transform:uppercase}
.step p{font-size:8px;line-height:14px;color:#cfc6bd;margin-top:10px}

/* services */
.services{height:390px;background:linear-gradient(160deg,#4e3c78 0%,#6a3f74 55%,#8a3c66 100%);color:var(--white)}
.band{position:absolute;top:30px;left:0}
.services-title{position:absolute;top:26px;width:100%;text-align:center;font:400 14px/20px "Roboto",Arial,sans-serif;text-transform:uppercase}
.service-list{position:absolute;top:112px;left:180px;display:flex;gap:10px}
.service{width:132px;text-align:center}
.service h3{font:500 12px/1 "Roboto",Arial,sans-serif;text-transform:uppercase;margin-top:22px;white-space:nowrap}
.service .btn{margin-top:8px;padding:6px 16px}

/* team */
.team{height:306px;padding-top:26px}
.team .body-copy{margin-top:10px}
.team .boxed-title{width:180px}
.members{position:absolute;top:124px;left:182px;display:flex;gap:14px}
.member{width:132px;height:160px;background:#f3ecec}
.member .portrait{height:126px}
.member h4{font:700 7px/1 "Open Sans",Arial,sans-serif;color:#333;text-align:center;margin-top:8px}
.member span{display:block;font-size:6px;color:var(--muted);text-align:center;margin-top:4px}

/* works */
.works{height:538px;background:var(--works)}
.works h2{position:absolute;top:28px;width:100%;text-align:center;font:400 14px/1 "Roboto",Arial,sans-serif;letter-spacing:3px;color:#9c98b4}
.filters{position:absolute;top:56px;width:100%;display:flex;justify-content:center;gap:20px;font:700 7px/1 "Roboto",Arial,sans-serif;letter-spacing:1px;color:#aaa6c2;text-transform:uppercase}
.gallery{position:absolute;top:80px;left:192px;display:grid;grid-template-columns:repeat(4,131px);grid-auto-rows:124px;gap:12px 2px}
.gallery div:nth-child(1){background:linear-gradient(160deg,#c7a070,#7a4a2c 60%,#a12a2a)}
.gallery div:nth-child(2){background:linear-gradient(160deg,#e6e0d6,#9a8a78)}
.gallery div:nth-child(3){background:linear-gradient(160deg,#6a5a4c,#ece6e0 60%,#2a2628)}
.gallery div:nth-child(4){background:linear-gradient(160deg,#8a6a42,#2a2426 60%,#d8d0c8)}
.gallery div:nth-child(5){background:linear-gradient(160deg,#d8d2c8,#9a8272 60%,#b8443c)}
.gallery div:nth-child(6){background:linear-gradient(160deg,#e07a1e,#5a2230 60%,#1e1420)}
.gallery div:nth-child(7){background:linear-gradient(160deg,#5a1e2a,#e05a3a 50%,#3a2a5a)}
.gallery div:nth-child(8){background:linear-gradient(160deg,#d8d4be,#8a9a5a 60%,#c8b49a)}
.gallery div:nth-child(9){background:linear-gradient(160deg,#c8b89a,#8a5a4a 60%,#d8c4a8)}
.gallery div:nth-child(10){background:linear-gradient(160deg,#3a6a3a,#c8a060 50%,#e8e4dc)}
.gallery div:nth-child(11){background:linear-gradient(160deg,#6a5a4c,#ece6e0 60%,#2a2628)}
.gallery div:nth-child(12){background:linear-gradient(160deg,#8a6a42,#2a2426 60%,#d8d0c8)}

/* testimonial */
.testimonial{height:194px;background:var(--blue);border-top:2px solid #9ec8de;color:var(--white)}
.avatar{position:absolute;top:56px;left:444px;width:40px;height:40px;background:linear-gradient(180deg,#c9d4de,#3a4250)}
.quote{position:absolute;top:114px;left:250px;width:430px;text-align:center;font-size:8px;line-height:15px;font-style:italic}
.author{position:absolute;top:168px;width:100%;text-align:center;font-size:6px}
.arrow{position:absolute;top:108px;width:14px;height:14px;background:var(--pink);display:flex;align-items:center;justify-content:center}

/* contact */
.contact{height:360px;padding-top:20px}
.contact .boxed-title{width:180px}
.contact .body-copy{margin-top:16px;width:420px;font-size:7px;line-height:14px}
.map{position:absolute;top:128px;left:182px;width:276px;height:172px;background:linear-gradient(135deg,#e8e8ea,#d6d8dc)}
.form{position:absolute;top:128px;left:472px;width:276px}
.row{display:flex;gap:10px}
.field{height:18px;border:1px solid #d6d6d6;font-size:6px;color:#aaa;padding:5px 8px}
.field.name{width:146px}
.field.email{width:120px}
.field.message{margin-top:4px;height:112px}
.send{margin-top:20px;height:20px;background:var(--pink);color:var(--white);font:700 7px/20px "Roboto",Arial,sans-serif;text-align:center;text-transform:uppercase}

/* footer */
.footer{height:48px;background:var(--footer);display:flex;align-items:center;padding:0 180px 0 192px;color:#9a96b0;font-size:7px}
.footer .brand{font-size:8px;color:var(--white)}
.footer small{margin-left:auto;font-size:6px}
</style>
</head>
<body>
<main class="page">

  <nav class="nav section">
    <span class="brand">Vowline Events</span>
    <div class="nav-links"><span>Home</span><span>Our Services</span><span>Portfolio</span><span>Our Team</span><span>Contact Us</span></div>
  </nav>

  <header class="hero section" role="img" aria-label="Photo of a bride and groom walking down a church aisle">
    <h1 class="hero-title">MARRIAGE EVENTS</h1>
    <div class="hero-actions">
      <span class="btn">Our Services</span>
      <span class="btn outline">Click Here</span>
    </div>
  </header>

  <section class="about section center">
    <h2 class="boxed-title">About Company</h2>
    <p class="body-copy">We plan weddings, church programs, concerts and picnics across the United States and Canada. Our team handles every detail, from the first idea to the last dance, so you can enjoy the day with the people you love. Each event is shaped around your story, your guests and your budget, with careful planning and warm service at every step of the way.</p>
    <span class="btn">View More</span>
  </section>

  <section class="process section" role="img" aria-label="Background photo of a church interior with guests seated" >
    <h2>HOW DO WE DO ?</h2>
    <div class="rule"></div>
    <div class="steps">
      <div class="step">
        <div class="ring"></div>
        <h3>Plan</h3>
        <p>We listen to your ideas, set the budget and build a clear timeline for the day.</p>
      </div>
      <div class="step">
        <div class="ring filled"><svg width="20" height="20" viewBox="0 0 20 20"><path d="M4 10l4 4 8-9" fill="none" stroke="#fff" stroke-width="2.5"/></svg></div>
        <h3>Design</h3>
        <p>We shape the look, the venue, the flowers and the music to match your style.</p>
      </div>
      <div class="step">
        <div class="ring"><svg width="20" height="20" viewBox="0 0 20 20"><path d="M10 3v10M6 9l4 4 4-4M5 16h10" fill="none" stroke="#d9a85a" stroke-width="2"/></svg></div>
        <h3>Colloborate</h3>
        <p>We work with trusted vendors and keep you updated through every stage.</p>
      </div>
      <div class="step">
        <div class="ring"><svg width="22" height="16" viewBox="0 0 22 16"><path d="M2 2v12M2 10h18v4M6 10V7h14v3" fill="none" stroke="#d9a85a" stroke-width="2"/></svg></div>
        <h3>Execute</h3>
        <p>On the day we run the show so you and your guests can simply celebrate.</p>
      </div>
    </div>
  </section>

  <section class="services section">
    <svg class="band" width="930" height="30" viewBox="0 0 930 30" aria-hidden="true">
      <polygon points="0,0 412,0 388,30 0,30" fill="var(--green)"/>
      <polygon points="528,0 930,0 930,30 516,30" fill="var(--green)"/>
    </svg>
    <h2 class="services-title">Our<br>Services</h2>
    <div class="service-list">
      <div class="service">
        <svg width="132" height="152" viewBox="0 0 132 152" role="img" aria-label="Photo of a decorated church hall">
          <defs><linearGradient id="g1" x1="0" y1="0" x2="0" y2="1"><stop offset="0" stop-color="#d8c6b0"/><stop offset="1" stop-color="#7a4a3a"/></linearGradient></defs>
          <polygon points="66,0 132,38 132,114 66,152 0,114 0,38" fill="url(#g1)"/>
        </svg>
        <h3>Church Programs</h3><span class="btn">View More</span>
      </div>
      <div class="service">
        <svg width="132" height="152" viewBox="0 0 132 152" role="img" aria-label="Photo of a couple at a wedding ceremony">
          <defs><linearGradient id="g2" x1="0" y1="0" x2="1" y2="1"><stop offset="0" stop-color="#8a7a6a"/><stop offset=".5" stop-color="#e8e2dc"/><stop offset="1" stop-color="#2a2628"/></linearGradient></defs>
          <polygon points="66,0 132,38 132,114 66,152 0,114 0,38" fill="url(#g2)"/>
        </svg>
        <h3>Wedding Events</h3><span class="btn">View More</span>
      </div>
      <div class="service">
        <svg width="132" height="152" viewBox="0 0 132 152" role="img" aria-label="Photo of a musician on a lit concert stage">
          <defs><linearGradient id="g3" x1="0" y1="0" x2="1" y2="1"><stop offset="0" stop-color="#e8a030"/><stop offset=".5" stop-color="#7a2a3a"/><stop offset="1" stop-color="#2a1a3a"/></linearGradient></defs>
          <polygon points="66,0 132,38 132,114 66,152 0,114 0,38" fill="url(#g3)"/>
        </svg>
        <h3>Musical Concerts</h3><span class="btn">View More</span>
      </div>
      <div class="service">
        <svg width="132" height="152" viewBox="0 0 132 152" role="img" aria-label="Photo of friends at an outdoor picnic table">
          <defs><linearGradient id="g4" x1="0" y1="0" x2="0" y2="1"><stop offset="0" stop-color="#5a8a4a"/><stop offset=".5" stop-color="#c8a878"/><stop offset="1" stop-color="#e8e6e0"/></linearGradient></defs>
          <polygon points="66,0 132,38 132,114 66,152 0,114 0,38" fill="url(#g4)"/>
        </svg>
        <h3>Picnic Events</h3><span class="btn">View More</span>
      </div>
    </div>
  </section>

  <section class="team section center">
    <h2 class="boxed-title">Meet the Team</h2>
    <p class="body-copy">Our planners bring years of event experience and a real love for bringing people together. From quiet chapels to loud concert halls, they know how to turn a plan into a day your guests will remember. Meet the people who will stand beside you from the first call to the final toast.</p>
    <div class="members">
      <div class="member"><div class="portrait" role="img" aria-label="Portrait of Daniel Carver" style="background:linear-gradient(180deg,#e8e8e8,#3a3e48)"></div><h4>Daniel Carver</h4><span>Lead Planner</span></div>
      <div class="member"><div class="portrait" role="img" aria-label="Portrait of Lena Moreau" style="background:linear-gradient(180deg,#cfe4ee,#d8e0e6 60%,#c04a5a)"></div><h4>Lena Moreau</h4><span>Designer</span></div>
      <div class="member"><div class="portrait" role="img" aria-label="Portrait of Owen Hale" style="background:linear-gradient(180deg,#4a4a4e,#5a6a8a)"></div><h4>Owen Hale</h4><span>Coordinator</span></div>
      <div class="member"><div class="portrait" role="img" aria-label="Portrait of Clara Wynn" style="background:linear-gradient(180deg,#f0ecea,#c89a7a 60%,#f0e6e2)"></div><h4>Clara Wynn</h4><span>Manager</span></div>
    </div>
  </section>

  <section class="works section">
    <h2>Our works</h2>
    <div class="filters"><span>Church Programs</span><span>Wedding Events</span><span>Musical Concerts</span><span>Picnic Events</span></div>
    <div class="gallery" role="img" aria-label="Gallery of event photos: church interiors, wedding couples, concerts and picnics">
      <div></div><div></div><div></div><div></div>
      <div></div><div></div><div></div><div></div>
      <div></div><div></div><div></div><div></div>
    </div>
  </section>

  <section class="testimonial section">
    <span class="arrow" style="left:186px"><svg width="6" height="8" viewBox="0 0 6 8"><path d="M5 0L0 4l5 4z" fill="#fff"/></svg></span>
    <div class="avatar" role="img" aria-label="Client portrait"></div>
    <p class="quote">"The whole team made our wedding feel calm and easy. Every detail was ready before we even asked, the music was perfect and our guests still talk about the evening. We could not have wished for a kinder group of people."</p>
    <p class="author">Jenna Brooks</p>
    <span class="arrow" style="left:736px"><svg width="6" height="8" viewBox="0 0 6 8"><path d="M1 0l5 4-5 4z" fill="#fff"/></svg></span>
  </section>

  <section class="contact section center">
    <h2 class="boxed-title">Contact Us</h2>
    <p class="body-copy">Tell us about your event and we will get back to you within one business day with ideas, dates and a first plan.</p>
    <div class="map" role="img" aria-label="Street map showing the office location"></div>
    <div class="form">
      <div class="row"><div class="field name">Name</div><div class="field email">Email</div></div>
      <div class="field message">Enter your message</div>
      <div class="send">Send My Message</div>
    </div>
  </section>

  <footer class="footer section">
    <span class="brand">Vowline Events</span>
    <small>© 2015 all rights reserved</small>
  </footer>

</main>
</body>
</html>
```